Flyer-Design für Touristikportal
Zielgruppe
Wir sind ein Online Reise- und Touristikportal: www.wegfalke.de mit einer Auswahl und Vielfalt an Reisen, die es sonst nicht gibt. Unsere Zielgruppe sind alle reiseaffinen Personen im Alter von 25 - 80 Jahren.
Aufgabenstellung
Der DIN Lang Flyer MUSS ein Eyecatcher sein bzw. haben. Nichts standardmäßiges, nichts langweiliges, nicht billig wirkend. Man muß sofort erkennen um was es geht - Reisen, Touren, Aktivitäten. Evtl. ein knackiger Slogan, ein Bild, das Emotionen weckt? Der DIN Lang Flyer liegt in Geschäften, Apotheken etc. aus - er muß ansprechend wirken! Auf der Rückseite sollte stehen, was wir alles anbieten, jetzt nicht im Detail, aber einen guten Überblick!

```html
<!DOCTYPE html>
<html lang="de">
<head>
<meta charset="utf-8">
<title>Wegfalke – DIN Lang Flyer</title>
<link href="https://fonts.googleapis.com/css2?family=Lato:ital,wght@0,400;0,700;0,900;1,700&display=swap" rel="stylesheet">
<style>
:root{
  --teal:#5bb8b3;
  --teal-text:#4fb0ab;
  --ink:#2b2b2b;
  --grey:#555;
  --paper:#ffffff;
  --rule:#c9c9c9;
}
*{margin:0;padding:0;box-sizing:border-box}
html,body{width:1008px;height:1200px;overflow:hidden;background:var(--paper)}
body{position:relative;font-family:'Lato',sans-serif;color:var(--ink)}
.sheet{position:absolute;left:30px;width:948px;height:237px;border:1px solid var(--rule);background:var(--paper)}
.panel{position:absolute;top:0;height:100%;overflow:hidden}
.photo-maldives{background:linear-gradient(180deg,#6f6aa8 0%,#b98fbf 28%,#f0b07a 45%,#4aa9b3 62%,#3a78a8 80%,#3b4f8e 100%)}
.photo-amalfi{background:linear-gradient(180deg,#8fd0e3 0%,#bfe3ea 30%,#d6a872 52%,#b37a4e 66%,#3aa3b0 82%,#1f7f91 100%)}
.photo-aurora{background:linear-gradient(180deg,#0d5f6e 0%,#3fc3bb 30%,#7ad8d0 48%,#b08a90 64%,#2a8e8a 80%,#0f5a62 100%)}
.headline{position:absolute;color:#fff;font-weight:900;line-height:1;text-transform:uppercase;white-space:nowrap}
.headline .small{font-weight:700;font-size:20px;display:block}
.headline .big{font-size:25px;display:block}
.headline.right{text-align:right}
.claim{position:absolute;color:#fff;font-weight:900;font-size:31px;line-height:.88;white-space:nowrap}
.claim.right{text-align:right}
.contact-panel{left:235px;width:478px}
.brand{position:absolute;left:0;right:0;text-align:center;font-weight:700;font-size:22px;letter-spacing:.5px;color:#3a3a3a}
.slogan{position:absolute;left:0;right:0;text-align:center;color:var(--teal-text);font-weight:700;font-size:10px;letter-spacing:.3px}
.contact{position:absolute;left:0;right:0;text-align:center;font-size:9.5px;line-height:1.2}
.contact .phone{font-weight:700}
.contact .hours{font-size:6px;color:var(--grey)}
.contact .mail{font-weight:700;margin-top:4px}
.contact .web{color:var(--teal-text);font-weight:700}
.folded{position:absolute;width:468px;height:237px;box-shadow:4px 4px 6px rgba(0,0,0,.35)}
.folded .fold{position:absolute;left:233px;top:0;width:1px;height:100%;background:rgba(255,255,255,.25)}
.label{position:absolute;font-size:15px;line-height:1.25;color:#1a1a1a}
.inside{position:absolute;left:30px;top:932px;width:948px;height:237px;background:var(--teal)}
.spread-shape{position:absolute;left:0;top:0}
.inside-title{position:absolute;left:25px;top:40px;color:#fff;font-weight:900;font-size:23px;line-height:1.04}
.inside-tagline{position:absolute;left:25px;top:184px;color:#fff;font-style:italic;font-weight:700;font-size:12.5px;line-height:1.3}
.inside-center{position:absolute;left:233px;width:480px;top:0;height:100%;text-align:center}
.inside-center .brand{top:38px}
.intro{position:absolute;left:0;right:0;top:90px;color:var(--teal-text);font-weight:700;font-size:9.8px;line-height:1.35}
.copy{position:absolute;left:0;right:0;top:124px;font-size:7.6px;line-height:1.55;color:#333}
.copy p+p{margin-top:3px}
.offers{position:absolute;left:720px;top:30px;width:220px;list-style:none}
.offers li{position:relative;display:flex;align-items:center;height:31.7px;padding-left:50px;color:#fff;font-weight:700;font-size:15px;letter-spacing:.6px;white-space:nowrap}
.offer-icon{position:absolute;top:3.85px;width:24px;height:24px}
</style>
</head>
<body>

<section class="sheet" style="top:30px">
  <div class="panel photo-maldives" style="left:0;width:235px" role="img" aria-label="Foto: Wasserbungalows am Steg bei Sonnenuntergang"></div>
  <div class="headline right" style="left:0;width:213px;top:167px"><span class="small">Wir sind</span><span class="big">Wegfalke</span></div>
  <div class="panel contact-panel">
    <div class="brand" style="top:38px">WEGFALKE</div>
    <div class="slogan" style="top:114px">Komm mit uns dem Himmel einfach etwas näher – nicht nur per Flieger!</div>
    <div class="contact" style="top:166px">
      <div class="phone">+49 30 / 5521 907 0</div>
      <div class="hours">(Mo – Sa von 07.00 bis 20.00)</div>
      <div class="mail">info@wegfalke.de</div>
      <div class="web">www.wegfalke.de</div>
    </div>
  </div>
  <div class="panel photo-maldives" style="left:713px;width:235px" role="img" aria-label="Foto: Reihe von Wasserbungalows im Abendlicht"></div>
  <div class="headline" style="left:736px;top:145px"><span class="small">Wir sind</span><span class="big">Voller</span><span class="big">Reisevielfalt</span></div>
</section>

<section class="folded photo-maldives" style="left:30px;top:245px" role="img" aria-label="Foto: Steg zu Wasserbungalows bei Sonnenuntergang">
  <div class="fold"></div>
  <div class="headline" style="left:21px;top:145px"><span class="small">Wir sind</span><span class="big">Voller</span><span class="big">Reisevielfalt</span></div>
  <div class="headline right" style="right:21px;top:168px"><span class="small">Wir sind</span><span class="big">Wegfalke</span></div>
</section>

<div class="label" style="left:510px;top:286px">Front/Rück Version 1<br>&lt;- zusammengefaltet</div>

<section class="sheet" style="top:637px">
  <div class="panel photo-aurora" style="left:0;width:235px" role="img" aria-label="Foto: Polarlichter über Bergen am Meer"></div>
  <div class="claim right" style="left:0;width:219px;top:158px">ENTDECKE<br>DIE VIELFALT.</div>
  <div class="panel contact-panel">
    <div class="brand" style="top:38px">WEGFALKE</div>
    <div class="slogan" style="top:114px">Komm mit uns dem Himmel einfach etwas näher – nicht nur per Flieger!</div>
    <div class="contact" style="top:166px">
      <div class="phone">+49 30 / 5521 907 0</div>
      <div class="hours">(Mo – Sa von 07.00 bis 20.00)</div>
      <div class="mail">info@wegfalke.de</div>
      <div class="web">www.wegfalke.de</div>
    </div>
  </div>
  <div class="panel photo-amalfi" style="left:713px;width:235px" role="img" aria-label="Foto: Küstenort an Felsklippen am Meer"></div>
  <div class="claim" style="left:736px;top:26px">ERLEBNIS<br>REISE.</div>
</section>

<div class="label" style="left:30px;top:606px">Front/Rück Version 2</div>
<div class="label" style="left:357px;top:606px">zusammengefaltet -&gt;</div>

<section class="folded" style="left:510px;top:426px">
  <div class="panel photo-amalfi" style="left:0;width:234px" role="img" aria-label="Foto: Küstenort an Felsklippen am Meer"></div>
  <div class="panel photo-aurora" style="left:234px;width:234px" role="img" aria-label="Foto: Polarlichter über Bergen am Meer"></div>
  <div class="claim" style="left:21px;top:26px">ERLEBNIS<br>REISE.</div>
  <div class="claim right" style="right:15px;top:158px">ENTDECKE<br>DIE VIELFALT.</div>
</section>

<div class="label" style="left:30px;top:901px">Variante für den Innenteil</div>

<section class="inside">
  <svg class="spread-shape" width="948" height="237" viewBox="0 0 948 237" aria-hidden="true">
    <path d="M233,0 Q183,118.5 233,237 L715,237 Q703,118.5 715,0 Z" fill="#fff"/>
  </svg>
  <h2 class="inside-title">FINDE UND<br>GENIESSE<br>URLAUB UND<br>ERLEBNISSE<br>WELTWEIT.</h2>
  <p class="inside-tagline">Wir stehen für Liebe<br>zum Detail und Qualität.</p>
  <div class="inside-center">
    <div class="brand">WEGFALKE</div>
    <p class="intro">Wir sind das Reiseportal für die schönsten Reiseziele weltweit.<br>Mit mehr als 50 Rubriken bieten wir eine einzigartige Vielfalt an Reisethemen.</p>
    <div class="copy">
      <p>Lass Dich inspirieren, durchstöbere unser vollgepacktes Reise- und Touristikportal und wähle aus dem<br>Angebot renommierter großer und kleiner Reiseveranstalter weltweit. Zusätzlich bieten wir eine ebenso einzigartige<br>Auswahl an Tickets für Aktivitäten, Touren, Sehenswürdigkeiten und Musikevents und Veranstaltungen weltweit.</p>
      <p>Damit Du auch ganz unbeschwert an Dein Reiseziel kommst, findest Du natürlich dank einer Flug-, Hotel-, Mietwagen-<br>und VISA Online Recherche Möglichkeit, ein Rundum-Sorglos-Paket, dass selbstverständlich auch über unsere Partner<br>buchbar ist. Wenn Du Dich zuerst inspirieren lassen möchtest, dann blättere doch spontan in unserem eigens<br>geschriebenen Reisemagazin mit netten Insidern und pfiffigen Sporttipps.</p>
    </div>
  </div>
  <ul class="offers">
    <li><svg class="offer-icon" style="left:0" viewBox="0 0 24 24" fill="none" stroke="#fff" stroke-width="1.2"><circle cx="12" cy="12" r="11"/><circle cx="12" cy="12" r="6.5"/><path d="M5.5 12h13M12 5.5c2.5 2.5 2.5 10.5 0 13M12 5.5c-2.5 2.5-2.5 10.5 0 13"/></svg>Themenreisen</li>
    <li><svg class="offer-icon" style="left:8px" viewBox="0 0 24 24" fill="none" stroke="#fff" stroke-width="1.2"><circle cx="12" cy="12" r="11"/><path d="M7 17l10-10M9 8l6 1M15 15l-1-6M8 14l-1 3 3-1"/></svg>Flüge</li>
    <li><svg class="offer-icon" style="left:13px" viewBox="0 0 24 24" fill="none" stroke="#fff" stroke-width="1.2"><circle cx="12" cy="12" r="11"/><path d="M12 5.5l2 4.2 4.5.5-3.3 3 .9 4.5-4.1-2.3-4.1 2.3.9-4.5-3.3-3 4.5-.5z"/></svg>Aktivitäten/Touren</li>
    <li><svg class="offer-icon" style="left:13px" viewBox="0 0 24 24" fill="none" stroke="#fff" stroke-width="1.2"><circle cx="12" cy="12" r="11"/><path d="M6 17V9M6 14h12v3M8 12h3v2M12 12h5a1 1 0 0 1 1 1v1"/></svg>Hotels</li>
    <li><svg class="offer-icon" style="left:8px" viewBox="0 0 24 24" fill="none" stroke="#fff" stroke-width="1.2"><circle cx="12" cy="12" r="11"/><rect x="6.5" y="7.5" width="11" height="10"/><path d="M6.5 10h11M9 6v3M15 6v3M9 12.5h1M12 12.5h1M15 12.5h1M9 15h1M12 15h1"/></svg>Events</li>
    <li><svg class="offer-icon" style="left:0" viewBox="0 0 24 24" fill="none" stroke="#fff" stroke-width="1.2"><circle cx="12" cy="12" r="11"/><path d="M6 15v-3l2-3.5h8l2 3.5v3zM6 15v1.5h2V15M16 15v1.5h2V15M6 12h12"/><circle cx="8.5" cy="13.5" r=".6"/><circle cx="15.5" cy="13.5" r=".6"/></svg>Mietwagen</li>
  </ul>
</section>

</body>
</html>
```